BlueMeadow Advisory LLC
Stationery and business card design
A winner has been decided. Thanks to everyone for all of your hard work! I had a tough time choosing among the great designs.
All,
Here are details on the logo font and color:
Colors:
1. PANTONE 1797 C (red)
2. Black: C=100, M=100, Y=100, K=100
Fonts:
1. HandelGotDBol >> "Blue"
2. HandelGotDBol >> "Meadow"
3. Agency FB >> "ADVISORY"
Thanks for your help!
Anyone know the font use in the logo?
PH please tell me the font name.
Here are some general comments on what I like and don't like so far:
1. I prefer straight lines and block format versus wavy lines.
2. I prefer more whitespace over solid color. However, I like a solid red color on the back of the business card.
3. I would prefer to stick to two colors (red and black) to reduce printing costs.
4. I prefer solid colors instead of using a gradual shading of a color.
Thanks for all of your help so far!
To ALL designers:
Thank you for your submissions so far! I want to clarify the contact information I'd like to see on each piece of stationery:
1. Business card - Should include all contact information EXCEPT for address. Be sure it includes both the Phone and Direct numbers per my earlier comment.
2. Letter - Should include: Address, Phone (555.201.4417), Website.
3. Envelope - Should include the Address only on the front. The back can have the Website.
Thanks.
A rating of one-star means I don't think you're on the right track. No stars mean I've yet to review the design. If I give more than one-star, you can expect me to clarify additional changes. I'll eliminate anything that doesn't have the correct text.
Thanks for your work so far! A couple changes to the contact info and design please:
1. Please capitalize the "C" in Dana on the email to be: Dana@BlueMeadowAdvisory.example
2. Please include two phone numbers:
Phone: 555.201.4417
Direct: 555.319.2785
3. Please design the business cards to be printed on a typical square card stock (not rounded edges).
Thanks!
Dana

```html
<!DOCTYPE html>
<html lang="en">
<head>
<meta charset="utf-8">
<title>BlueMeadow Advisory – Stationery</title>
<link href="https://fonts.googleapis.com/css2?family=Saira:wght@700&family=Open+Sans:wght@400;600&display=swap" rel="stylesheet">
<style>
  :root{
    --red:#d9232c;
    --black:#111111;
    --paper:#ffffff;
    --sky:#8ed4e6;
    --ink-soft:#555555;
    --rule:#cfcfcf;
  }
  *{box-sizing:border-box;margin:0;padding:0}
  html,body{width:1200px;height:518px;overflow:hidden;background:#ffffff}
  body{font-family:"Open Sans",sans-serif;color:var(--black);position:relative}
  .stage{position:absolute;left:19px;top:19px;width:1162px;height:485px;background:var(--sky);border-radius:22px}
  .piece{position:absolute;background:var(--paper);box-shadow:0 1px 3px rgba(0,0,0,.25);overflow:hidden}
  .wordmark{font-family:"Saira",sans-serif;font-weight:700;color:var(--black);white-space:nowrap;line-height:1}
  .wordmark .mark-square{display:inline-block;background:var(--red);vertical-align:middle;margin-right:5px}
  .fine{font-size:5px;line-height:1.5;color:var(--ink-soft)}
  /* business cards */
  .card-front{width:139px;height:79px}
  .card-front .wordmark{position:absolute;left:9px;top:10px;font-size:11px}
  .card-front .wordmark .mark-square{width:8px;height:8px}
  .card-front .holder{position:absolute;left:9px;top:34px}
  .card-front .holder-name{font-size:6.5px;font-weight:600;color:var(--black)}
  .card-front .top-strip{position:absolute;left:0;top:0;width:100%;height:4px;background:var(--black)}
  .card-back{width:135px;height:79px;background:var(--red)}
  .card-back .web{position:absolute;left:0;right:0;bottom:22px;text-align:center;font-size:5.5px;color:#fff}
  /* envelopes */
  .envelope{width:291px;height:185px}
  .envelope .band-top{position:absolute;left:0;top:0;width:100%;height:30px;background:var(--red)}
  .envelope .band-bottom{position:absolute;left:0;bottom:0;width:100%;height:7px;background:var(--red)}
  .envelope .wordmark{position:absolute;left:12px;top:120px;font-size:15px}
  .envelope .wordmark .mark-square{width:11px;height:11px}
  .envelope .return-address{position:absolute;left:12px;top:140px}
  .envelope-back{width:291px;height:144px}
  .envelope-back .flap{position:absolute;left:0;top:0;width:100%;height:38px;background:var(--red)}
  .envelope-back .web{position:absolute;left:0;right:0;top:15px;text-align:center;font-size:6px;color:#fff}
  .envelope-back .window{position:absolute;left:76px;top:102px;width:84px;height:24px;border:1px solid var(--rule);background:#f6f6f6}
  /* letterheads */
  .letterhead{width:226px;height:331px}
  .letterhead .wordmark{position:absolute;left:12px;top:14px;font-size:14px}
  .letterhead .wordmark .mark-square{width:10px;height:10px}
  .letterhead .footer{position:absolute;left:0;bottom:0;width:100%;height:20px;background:var(--black);color:#fff;font-size:5px;padding:7px 12px}
  .letterhead .footer-rule{position:absolute;left:0;bottom:20px;width:100%;height:3px;background:var(--red)}
</style>
</head>
<body>
<main class="stage">

  <!-- business card set one -->
  <section class="piece card-front" style="left:34px;top:46px">
    <div class="wordmark"><span class="mark-square"></span>BlueMeadow</div>
    <div class="holder">
      <p class="holder-name">Dana Bramlet</p>
      <p class="fine">Principal<br>Phone: 555.201.4417<br>Direct: 555.319.2785<br>Dana@BlueMeadowAdvisory.example</p>
    </div>
  </section>
  <section class="piece card-back" style="left:187px;top:46px">
    <p class="web">www.BlueMeadowAdvisory.example</p>
  </section>

  <!-- business card set two -->
  <section class="piece card-front" style="left:336px;top:46px">
    <div class="top-strip"></div>
    <div class="wordmark"><span class="mark-square"></span>BlueMeadow</div>
    <div class="holder">
      <p class="holder-name">Dana Bramlet</p>
      <p class="fine">Principal<br>Phone: 555.201.4417<br>Direct: 555.319.2785<br>Dana@BlueMeadowAdvisory.example</p>
    </div>
  </section>
  <section class="piece card-back" style="left:485px;top:46px">
    <p class="web">www.BlueMeadowAdvisory.example</p>
  </section>

  <!-- envelopes -->
  <section class="piece envelope" style="left:34px;top:132px">
    <div class="band-top"></div>
    <div class="wordmark"><span class="mark-square"></span>BlueMeadow</div>
    <p class="fine return-address">410 Orchard Lane, Suite 2, Springfield</p>
    <div class="band-bottom"></div>
  </section>
  <section class="piece envelope" style="left:336px;top:132px;height:170px">
    <div class="band-top"></div>
    <div class="wordmark"><span class="mark-square"></span>BlueMeadow</div>
    <p class="fine return-address">410 Orchard Lane, Suite 2, Springfield</p>
    <div class="band-bottom"></div>
  </section>
  <section class="piece envelope-back" style="left:336px;top:312px">
    <div class="flap"></div>
    <p class="web">www.BlueMeadowAdvisory.example</p>
    <div class="window"></div>
  </section>

  <!-- letterheads -->
  <section class="piece letterhead" style="left:648px;top:46px">
    <div class="wordmark"><span class="mark-square"></span>BlueMeadow</div>
    <div class="footer-rule"></div>
    <p class="footer">410 Orchard Lane, Suite 2, Springfield &nbsp;|&nbsp; 555.201.4417 &nbsp;|&nbsp; www.BlueMeadowAdvisory.example</p>
  </section>
  <section class="piece letterhead" style="left:886px;top:46px">
    <div class="wordmark"><span class="mark-square"></span>BlueMeadow</div>
    <div class="footer-rule"></div>
    <p class="footer">410 Orchard Lane, Suite 2, Springfield &nbsp;|&nbsp; 555.201.4417 &nbsp;|&nbsp; www.BlueMeadowAdvisory.example</p>
  </section>

</main>
</body>
</html>
```